Cheeky, Playful, Homebrew Beer Label

I homebrew as a hobby and am creating a beer in honor of my partner's stuffed animal. His name is Gorvik, he is an elephant, and he likes to drink. The beer is a Belgian style Tripel called "Gorvik's Tripel Tumble"

I am looking for a label for this beer. Ideally, the artwork will be in a form I can scale up to print on an A3 size piece of paper as well.

I would like the label to be an illustration, playful in nature, and potentially adult in theme, the elephant likes to drink after all. He could be swimming in a giant goblet of beer, drunk and collapsed, or something else entirely, as long as there's some implication that he is drinking. Please make sure he resembles the picture. I'd also like there to be some reference to three since the beer is a tripel. Because a tripel is blonde / straw-ish in color, some element of the label should reflect that.

The elephant is lighthearted, we're lighthearted and silly at times, this should be too.

Photo of the Gorvik the Elephant is attached, as is the beer label template. Also including part of a Thanksgiving invitation I made with photoshop just in case it sparks anything.
Updates

Hi there, Please be sure any illustration of an Elephant resembles the picture of Gorvik. I've also come across this old national park poster, and I am a fan of the layout: http://loomvale.example-blog.com/loomvale/images/2007/12/09/picture_2.png Thanks,

Industry/Entity Type

Adult

Font styles to use
Other font styles liked:
• Dapper Walrus

Requirements
Must have
• Gorvik the elephant
Reference to beer / drinking (bottles, goblets, glasses, etc.)
Incorporation of something to do with the number three. Can be symbolic not literal
Should not have
• Anything too serious or dramatic

```html
<!DOCTYPE html>
<html lang="en">
<head>
<meta charset="utf-8">
<title>Gorvik's Tripel Tumble – Beer Label</title>
<link rel="stylesheet" href="https://fonts.googleapis.com/css2?family=Londrina+Solid:wght@400;900&family=Oswald:wght@300&display=swap">
<style>
  :root {
    --paper: #e4ddcc;
    --paper-edge: #d9cfb6;
    --frame-gold: #c4921c;
    --ink: #1f1a15;
    --ink-glow: #f4dc8e;
    --mustard: #d9b21f;
    --banner-red: #a8151a;
    --banner-shade: #7e0f13;
    --banner-text: #f6c94a;
    --star-green: #1d7a2e;
    --caption: #9b7a3c;
  }
  * { margin: 0; padding: 0; box-sizing: border-box; }
  html, body {
    width: 1059px; height: 1200px; overflow: hidden;
    background: var(--paper);
  }
  .label {
    position: relative; width: 1059px; height: 1200px;
    background: radial-gradient(ellipse at center, var(--paper) 55%, var(--paper-edge) 100%);
  }
  .label-frame {
    position: absolute; left: 36px; top: 36px; width: 988px; height: 1128px;
    border: 3px solid var(--frame-gold);
    box-shadow: inset 0 0 18px rgba(196, 146, 28, 0.35);
  }
  .mascot-art {
    position: absolute; left: 350px; top: 178px; width: 310px; height: 256px;
    border-radius: 40% 40% 50% 50% / 30% 30% 22% 22%;
    background: linear-gradient(180deg, var(--ink) 0%, var(--ink) 70%, var(--mustard) 100%);
  }
  .brand-name {
    position: absolute; left: 0; top: 448px; width: 1059px;
    text-align: center;
    font-family: "Londrina Solid", sans-serif; font-weight: 900;
    font-size: 250px; line-height: 1; letter-spacing: 4px;
    color: var(--ink);
    text-shadow: 5px 5px 0 var(--ink-glow);
  }
  .brand-name .possessive { font-size: 96px; vertical-align: 118px; letter-spacing: 0; }
  .tripel-stars { position: absolute; left: 440px; top: 716px; width: 180px; height: 50px; }
  .banner { position: absolute; left: 170px; top: 745px; width: 720px; height: 240px; }
  .banner-title {
    position: absolute; left: 0; top: 782px; width: 1059px; text-align: center;
    font-family: "Londrina Solid", sans-serif; font-weight: 900;
    font-size: 64px; line-height: 1; letter-spacing: 3px;
    color: var(--banner-text);
  }
  .style-line {
    position: absolute; left: 0; top: 918px; width: 1059px; text-align: center;
    font-family: "Oswald", sans-serif; font-weight: 300;
    font-size: 21px; letter-spacing: 4px; color: var(--caption);
  }
  .style-line .dot {
    display: inline-block; width: 7px; height: 7px; border-radius: 50%;
    background: var(--caption); vertical-align: middle; margin: 0 18px;
  }
</style>
</head>
<body>
  <main class="label">
    <div class="label-frame"></div>

    <div class="mascot-art" role="img" aria-label="Illustration of Gorvik the elephant spraying beer from his trunk, standing on a golden puddle"></div>

    <h1 class="brand-name">GORVIK<span class="possessive">'s</span></h1>

    <svg class="tripel-stars" viewBox="0 0 180 50" aria-hidden="true">
      <g fill="var(--star-green)">
        <polygon transform="translate(26 27) scale(0.8)" points="0,-20 5.9,-8.1 19,-6.2 9.5,3.1 11.8,16.2 0,10 -11.8,16.2 -9.5,3.1 -19,-6.2 -5.9,-8.1"/>
        <polygon transform="translate(90 24)" points="0,-20 5.9,-8.1 19,-6.2 9.5,3.1 11.8,16.2 0,10 -11.8,16.2 -9.5,3.1 -19,-6.2 -5.9,-8.1"/>
        <polygon transform="translate(154 27) scale(0.8)" points="0,-20 5.9,-8.1 19,-6.2 9.5,3.1 11.8,16.2 0,10 -11.8,16.2 -9.5,3.1 -19,-6.2 -5.9,-8.1"/>
      </g>
    </svg>

    <svg class="banner" viewBox="0 0 720 240" aria-hidden="true">
      <path class="banner-tail" fill="var(--banner-red)" d="M90 110 L40 122 L10 200 L150 225 L175 185 L140 150 Z"/>
      <path class="banner-tail" fill="var(--banner-red)" d="M630 110 L680 122 L710 200 L570 225 L545 185 L580 150 Z"/>
      <path class="banner-fold" fill="var(--banner-shade)" d="M90 110 L140 150 L110 145 Z M630 110 L580 150 L610 145 Z"/>
      <path class="banner-band" fill="var(--banner-red)" d="M60 40 Q360 5 660 40 L640 135 Q360 100 80 135 Z"/>
    </svg>
    <p class="banner-title">Tripel Tumble</p>

    <p class="style-line"><span class="dot"></span>BELGIUM STYLE TRIPEL<span class="dot"></span></p>
  </main>
</body>
</html>
```